Business Card Design job - Tyre Shop

Client wants a double sided business cards designed for a Tyre Shop.

The logo can be used in multiple ways, some examples are attached.

The reference font is:
https://www.typebarrel.example/fonts/open-sans
Others can be applied.

Color scheme should be mainly black and white, and red as a third less used color.

Contact Information for Business Card

Required Fields (Portuguese language):
- Name "Artur Maldo"
- Title "Gerente"
- Phone "256 907 342"
- Website "www.rodalimpa.pt"
- Email "geral@rodalimpa.pt
- Address "Rua das Feiteiras N.187
4790-318 Quintela, Ribafria"

Font styles to use
Sans Serif

Requirements
Must have
• Corporate Logo
Nice to have
• The client would like the card to have special feature to measure the tyre tread, as shown in examples attached.
• The tread Values as Portuguese law are:
• - Ilegal - less than 1.6mm
• - change tyres - between 3mm and 1.6 mm
• - OK - above 3mm
• Card should be kept standard rectangle size 85x55mm

```html
<!DOCTYPE html>
<html lang="pt">
<head>
<meta charset="utf-8">
<title>Roda Limpa – Cartão de Visita</title>
<link href="https://fonts.googleapis.com/css2?family=Open+Sans:wght@400;600;700;800&display=swap" rel="stylesheet">
<style>
  :root {
    --backdrop: #2b2e34;
    --paper: #ffffff;
    --ink: #231f20;
    --band: #2a2b2e;
    --stripe-mid: #8a8f92;
    --stripe-light: #b9bdbf;
    --accent-red: #ee1c25;
    --accent-pink: #f25a8a;
  }
  * { box-sizing: border-box; margin: 0; padding: 0; }
  html, body { width: 1200px; height: 1200px; overflow: hidden; }
  body {
    background: var(--backdrop);
    font-family: "Open Sans", Arial, sans-serif;
    color: var(--ink);
    position: relative;
  }
  .card {
    position: absolute;
    left: 190px;
    width: 820px;
    height: 531px;
    background: var(--paper);
    overflow: hidden;
  }
  .card--front { top: 46px; }
  .card--back { top: 623px; }
  .card__band { position: absolute; left: 0; bottom: 0; width: 820px; }

  /* Front */
  .front__brand {
    position: absolute;
    left: 0; right: 0; top: 150px;
    display: flex; flex-direction: column; align-items: center;
  }
  .brand-mark { display: flex; align-items: center; gap: 22px; }
  .brand-mark__dot {
    width: 74px; height: 74px; border-radius: 50%;
    background: var(--ink);
  }
  .brand-mark__name {
    font-weight: 800; font-size: 86px; letter-spacing: -2px;
    text-transform: uppercase; line-height: 1; color: var(--ink);
  }
  .front__tagline {
    margin-top: 14px;
    font-weight: 700; font-size: 11.5px; letter-spacing: 4px;
    text-transform: uppercase; color: var(--ink);
  }

  /* Back */
  .back__brand {
    position: absolute; left: 60px; top: 140px; width: 300px;
    display: flex; flex-direction: column; align-items: center; gap: 18px;
  }
  .back__brand .brand-mark__name { font-size: 52px; letter-spacing: -1px; text-align: center; line-height: 0.95; }
  .back__brand .brand-mark__dot { width: 96px; height: 96px; }
  .back__divider {
    position: absolute; left: 410px; top: 80px;
    width: 3px; height: 270px; background: var(--accent-red);
  }
  .contact {
    position: absolute; right: 60px; top: 88px;
    text-align: right;
  }
  .contact__name { font-weight: 600; font-size: 34px; line-height: 1.2; }
  .contact__role { font-size: 24px; margin-top: 6px; }
  .contact__lines { font-size: 24px; line-height: 1.3; margin-top: 14px; }
  .contact__address { font-size: 24px; line-height: 1.3; margin-top: 10px; }
  .back__website {
    position: absolute; left: 60px; bottom: 80px;
    color: var(--paper); font-weight: 600; font-size: 27px; letter-spacing: 2px;
  }
</style>
</head>
<body>

<section class="card card--front" aria-label="Frente do cartão">
  <div class="front__brand">
    <div class="brand-mark">
      <span class="brand-mark__dot"></span>
      <span class="brand-mark__name">Roda Limpa</span>
    </div>
    <p class="front__tagline">Especialista em pneus &amp; manutenção automóvel</p>
  </div>
  <svg class="card__band" height="120" viewBox="0 0 820 120" aria-hidden="true">
    <polygon points="0,0 520,0 600,120 0,120" fill="var(--band)"/>
    <polygon points="540,22 595,22 661,120 606,120" fill="var(--stripe-mid)"/>
    <polygon points="615,22 665,22 731,120 681,120" fill="var(--stripe-light)"/>
    <polygon points="685,22 710,22 776,120 751,120" fill="var(--accent-red)"/>
    <polygon points="728,22 746,22 812,120 794,120" fill="var(--accent-pink)"/>
  </svg>
</section>

<section class="card card--back" aria-label="Verso do cartão">
  <div class="back__brand">
    <span class="brand-mark__name">Roda<br>Limpa</span>
    <span class="brand-mark__dot"></span>
  </div>
  <div class="back__divider"></div>
  <div class="contact">
    <p class="contact__name">Artur Maldo</p>
    <p class="contact__role">Gerente</p>
    <p class="contact__lines">256 907 342<br>geral@rodalimpa.pt</p>
    <p class="contact__address">Rua das Feiteiras N.187<br>4790-318 Quintela, Ribafria</p>
  </div>
  <svg class="card__band" height="150" viewBox="0 0 820 150" aria-hidden="true">
    <polygon points="0,0 400,0 500,150 0,150" fill="var(--band)"/>
    <polygon points="470,62 570,62 629,150 529,150" fill="var(--stripe-mid)"/>
    <polygon points="590,72 660,72 713,150 643,150" fill="var(--stripe-light)"/>
    <polygon points="680,80 720,80 768,150 728,150" fill="var(--accent-red)"/>
    <polygon points="740,85 770,85 814,150 784,150" fill="var(--accent-pink)"/>
  </svg>
  <p class="back__website">www.rodalimpa.pt</p>
</section>

</body>
</html>
```